Business Card Design

We are a Sydney based bespoke Concierge company, providing hospitality services including Concierge staffing, catering, home dining, events, delivery, stallorix, and manage desks in residential apartment services. Our website goes into more detail.

Target Market(s)

corporate clients, upscale residential clients, executives,

Industry/Entity Type

Hospitality

Contact Information for Business Card

David SouthwellDirector of Operations & Customer Experience
Marlowe Concierge
W:www.marloweconcierge-demo.net;
E;peter@marloweconcierge-demo.net
M: 0412 907 281

Font styles to use
Serif

Colors
3176b5
85cae6
d2a4cc
6b449b

Requirements
Must have
• Business name
• Name
• Title
• Tel
• Email
• Website
Nice to have
• Back - facebook , twitter, instagram

```html
<!DOCTYPE html>
<html lang="en">
<head>
<meta charset="utf-8">
<title>Marlowe Concierge – Business Card</title>
<link rel="stylesheet" href="https://fonts.googleapis.com/css2?family=Cinzel:wght@600&family=Open+Sans:wght@400&display=swap">
<style>
  :root {
    --stage: #d9d6d2;
    --purple-light: #8e6fb6;
    --purple: #6b449b;
    --purple-dark: #45286f;
    --ink: #2b2b2b;
    --paper: #ffffff;
    --band-grey: #e4e2e6;
  }
  * { margin: 0; padding: 0; box-sizing: border-box; }
  html, body { width: 1200px; height: 871px; overflow: hidden; }
  body { background: var(--stage); position: relative; font-family: "Open Sans", sans-serif; }

  .card {
    position: absolute;
    width: 540px; height: 309px;
    border-radius: 3px;
    box-shadow: 0 8px 22px rgba(0,0,0,.22);
    overflow: hidden;
  }

  /* Back */
  .card-back {
    left: 70px; top: 100px;
    background: linear-gradient(100deg, var(--purple-light) 0%, var(--purple) 55%, var(--purple-dark) 100%);
  }
  .card-back .brand-name {
    position: absolute; left: 36px; bottom: 66px;
    font-family: "Open Sans", sans-serif; font-weight: 400;
    color: var(--paper); font-size: 28px; line-height: 1.2;
    white-space: nowrap;
  }
  .card-back .base-band {
    position: absolute; left: 36px; right: 220px; bottom: 18px; height: 22px;
    background: var(--band-grey);
  }
  .card-back .social {
    position: absolute; right: 34px; bottom: 150px;
    display: flex; align-items: center; gap: 10px;
    color: var(--paper); font-size: 16px; letter-spacing: .3px;
  }
  .card-back .social-mark {
    width: 14px; height: 14px; border-radius: 50%; background: var(--paper);
  }

  /* Front */
  .card-front {
    left: 590px; top: 450px;
    background: linear-gradient(160deg, #ffffff 60%, #f1f1f1 100%);
  }
  .card-front .top-band {
    position: absolute; left: 150px; top: 0; width: 205px; height: 24px;
    background: linear-gradient(90deg, var(--purple-light), var(--purple));
  }
  .card-front .brand-name {
    position: absolute; left: 150px; top: 44px;
    font-family: "Open Sans", sans-serif; font-weight: 400;
    color: var(--purple); font-size: 28px; line-height: 1.2;
    white-space: nowrap;
  }

  .card-front .details {
    position: absolute; left: 262px; top: 166px;
  }
  .card-front .person-name {
    font-family: "Cinzel", serif; font-weight: 600; color: var(--ink);
    font-size: 19px; letter-spacing: 1px;
  }
  .card-front .person-title {
    color: var(--purple); font-size: 13px; margin-top: 1px; margin-bottom: 14px;
  }
  .card-front .contact-list { list-style: none; }
  .card-front .contact-list li {
    display: flex; align-items: center; gap: 10px;
    color: var(--ink); font-size: 13px; line-height: 21px;
  }
  .card-front .contact-list svg { width: 14px; height: 14px; flex: none; }
</style>
</head>
<body>

<section class="card card-back" aria-label="Business card, back">
  <div class="brand-name">Marlowe Concierge</div>
  <div class="base-band"></div>
  <div class="social">
    <span class="social-mark" aria-hidden="true"></span>
    <span class="social-handle">marloweconcierge</span>
  </div>
</section>

<section class="card card-front" aria-label="Business card, front">
  <div class="top-band"></div>
  <div class="brand-name">Marlowe Concierge</div>
  <div class="details">
    <div class="person-name">Peter Hollingby</div>
    <div class="person-title">Director of Operations</div>
    <ul class="contact-list">
      <li>
        <svg viewBox="0 0 16 16" aria-hidden="true"><path d="M2 6c0-2 3-3 6-3s6 1 6 3l-2 1-1-2H5L4 7 2 6zM4 8h8l1 5H3l1-5z" fill="#6b449b"/><circle cx="8" cy="10.5" r="1.5" fill="#fff"/></svg>
        <span>0412 907 281</span>
      </li>
      <li>
        <svg viewBox="0 0 16 16" aria-hidden="true"><rect x="1.5" y="3.5" width="13" height="9" fill="none" stroke="#6b449b" stroke-width="1.4"/><path d="M1.5 3.5 8 9l6.5-5.5" fill="none" stroke="#6b449b" stroke-width="1.4"/></svg>
        <span>peter@marloweconcierge-demo.net</span>
      </li>
      <li>
        <svg viewBox="0 0 16 16" aria-hidden="true"><circle cx="8" cy="8" r="6.3" fill="none" stroke="#6b449b" stroke-width="1.4"/><ellipse cx="8" cy="8" rx="2.8" ry="6.3" fill="none" stroke="#6b449b" stroke-width="1.2"/><path d="M1.7 8h12.6" stroke="#6b449b" stroke-width="1.2"/></svg>
        <span>www.marloweconcierge-demo.net</span>
      </li>
    </ul>
  </div>
</section>

</body>
</html>
```